Wordpress Design Project

Need a page like this but with your own personal twist

I will provide you the iframed form on 2nd page

http://www.plumcovesaver.net/index1178.php?subid=8715815

Requirements
Must have
• Article with link out
must pass zipcode to iframed form on 2nd page.

Must provide css for form pages.

```html
<!DOCTYPE html>
<html lang="en">
<head>
<meta charset="utf-8">
<title>Auto Insurance – Save Big</title>
<link rel="stylesheet" href="https://fonts.googleapis.com/css2?family=Oswald:wght@400;500;700&family=Oxygen:wght@300;400&family=Yanone+Kaffeesatz:wght@400;600&display=swap">
<style>
:root{
  --navy:#022a55;
  --navy-deep:#0a1a33;
  --blue:#0e4a8c;
  --step-dark:#3a3d42;
  --red:#d4202a;
  --ink:#1e1e1e;
  --brand:#333333;
  --line:#c9c9c9;
  --panel:#ececec;
  --white:#ffffff;
  --link:#3b5998;
}
*{box-sizing:border-box;margin:0;padding:0}
html,body{width:1200px;height:1181px;overflow:hidden}
body{background:var(--navy);position:relative;font-family:Arial,Helvetica,sans-serif;color:var(--ink)}
.abs{position:absolute}
.page{left:130px;top:13px;width:941px;height:1112px;background:var(--white)}
.header-tex{left:130px;top:13px;width:941px;height:230px;
  background:repeating-linear-gradient(45deg,#fafafa 0 2px,#f2f2f2 2px 4px)}
.brand-name{left:154px;top:36px;font-family:'Oxygen',sans-serif;font-weight:400;font-size:36px;color:var(--brand);line-height:1;white-space:nowrap}
.tagline{left:154px;top:80px;font-family:'Oxygen',sans-serif;font-size:14px;letter-spacing:2.4px;color:#444}
.call{left:805px;top:22px;font-family:'Oswald',sans-serif;font-size:24px;color:#333}
.call b{color:var(--red);font-weight:400}
.hero-frame{left:152px;top:130px;width:893px;height:236px;border:1px solid var(--line);border-bottom:none}
.save{left:161px;top:128px;font-family:'Oswald',sans-serif;font-weight:700;font-size:62px;color:var(--red);line-height:1.1}
.rate{left:161px;top:190px;font-family:'Oswald',sans-serif;font-size:27px;color:#2b2b2b;white-space:nowrap}
.rate b{font-size:36px;font-weight:700}
.car{left:632px;top:60px;width:425px;height:180px;border-radius:10px;
  background:linear-gradient(180deg,#f4f5f6 0%,#c9ccd0 55%,#8d9094 100%)}
.band{left:0;top:241px}
.step-label{top:265px;font-family:'Oswald',sans-serif;font-weight:700;font-size:58px;color:var(--white);text-shadow:0 2px 3px rgba(0,0,0,.35)}
.content-frame{left:152px;top:366px;width:893px;height:741px;border:1px solid var(--line);border-top:none}
.step-text{top:372px;width:320px;text-align:center;font-family:'Oxygen',sans-serif;font-weight:300;font-size:28px;line-height:33px;color:#333}
.step-text b{color:var(--red);font-weight:400}
.zip-panel{left:180px;top:458px;width:836px;height:83px;background:var(--panel);border:1px solid var(--line);border-radius:4px}
.zip-label{left:213px;top:485px;font-family:'Oxygen',sans-serif;font-size:22px;color:#555}
.zip-input{left:471px;top:482px;width:183px;height:36px;background:var(--white);border:1px solid #bdbdbd;border-radius:4px;box-shadow:inset 0 1px 2px rgba(0,0,0,.1)}
.continue{left:668px;top:482px;width:147px;height:37px;border-radius:4px;background:linear-gradient(#e0262f,#b5141d);
  font-family:Arial,sans-serif;font-weight:700;font-size:21px;color:var(--white);display:flex;align-items:center;justify-content:center;gap:8px}
.continue i{width:16px;height:16px;border-radius:50%;background:var(--white);display:inline-block;position:relative}
.continue i::after{content:"";position:absolute;left:6px;top:4px;border-left:6px solid #c41b24;border-top:4px solid transparent;border-bottom:4px solid transparent}
.badge{left:862px;top:474px;width:128px;height:50px;background:#d9d9d9;border-radius:5px}
.section-title{font-family:'Yanone Kaffeesatz',sans-serif;font-size:28px;color:#222;white-space:nowrap}
.article{left:182px;top:613px;width:531px;font-size:14.6px;line-height:19px;text-align:justify;color:#111}
.article p{margin-bottom:19px}
.review{left:748px;top:608px;width:268px;height:142px;background:#ececec;border:1px solid #bdbdbd;border-radius:16px;
  padding:16px 18px;font-style:italic;font-size:14px;line-height:17px;color:#333}
.review-tail{left:962px;top:749px}
.reviewer{left:748px;top:778px;width:257px;text-align:right;font-style:italic;font-size:15px;color:var(--red)}
.fan-box{left:748px;top:817px;width:268px;height:271px;border:1px solid #aaa;background:var(--white);font-family:'Oxygen',sans-serif}
.fan-head{height:27px;background:#eceef4;border-bottom:1px solid #c4cde0;padding:6px 10px;font-size:12px;color:#333}
.fan-name{margin:10px 0 0 5px;font-size:14px;color:var(--link)}
.fan-name small{font-size:12px}
.fan-like{margin:2px 0 0 5px;font-size:10px;color:#333}
.fan-like span{color:var(--link)}
.fan-rule{margin:10px 5px 0;border-top:1px solid #ddd}
.fan-count{margin:6px 0 0 9px;font-size:10px;color:#333}
.fans{display:grid;grid-template-columns:repeat(5,45px);column-gap:5px;row-gap:6px;margin:5px 0 0 9px}
.fan{text-align:center;font-size:8.5px;color:#555}
.fan .ph{width:45px;height:44px;margin-bottom:3px;background:linear-gradient(160deg,#8a6a52,#4a3a30)}
.fan-foot{margin:6px 5px 0;border-top:1px solid #ddd;padding-top:6px;font-size:8.5px;color:#555;display:flex;align-items:center;gap:5px}
.fan-foot i{width:11px;height:11px;background:var(--link);display:inline-block}
.footer-nav{left:144px;top:1141px;font-family:'Oxygen',sans-serif;font-size:13px;color:#e6ecf4}
.footer-nav span{margin:0 10px}
.copyright{left:790px;top:1143px;font-family:'Oxygen',sans-serif;font-size:11px;color:#e6ecf4}
</style>
</head>
<body>
<div class="abs page"></div>
<div class="abs header-tex"></div>
<div class="abs brand-name">Auto Insurance</div>
<div class="abs tagline">YOUR PUNCH LINE GOSE HERE</div>
<div class="abs call">Call us: <b>555-014-2290</b></div>
<div class="abs hero-frame"></div>
<div class="abs save">Save Big!</div>
<div class="abs rate">on Your Auto Insurance as low as <b>$7/WEEK</b></div>
<div class="abs car" role="img" aria-label="Silver hatchback car photo"></div>

<svg class="abs band" width="1200" height="150" viewBox="0 0 1200 150" aria-hidden="true">
  <defs>
    <linearGradient id="silver" x1="0" y1="0" x2="0" y2="1">
      <stop offset="0" stop-color="#f4f4f4"/><stop offset=".5" stop-color="#d2d4d6"/><stop offset="1" stop-color="#eeeeee"/>
    </linearGradient>
  </defs>
  <rect x="0" y="0" width="1200" height="125" fill="url(#silver)"/>
  <rect x="107" y="0" width="989" height="125" fill="#0e4a8c"/>
  <polyline points="320,6 420,6 452,62 420,119 320,119" fill="none" stroke="#5a86b8" stroke-width="1.5"/>
  <polygon points="408,0 774,0 815,62 774,125 408,125 449,62" fill="#3a3d42"/>
  <polyline points="394,0 435,62 394,125" fill="none" stroke="#cdd1d6" stroke-width="10"/>
  <polyline points="790,0 831,62 790,125" fill="none" stroke="#cdd1d6" stroke-width="10"/>
  <polyline points="700,6 760,6 796,62 760,119 700,119" fill="none" stroke="#6c7076" stroke-width="1.5"/>
  <polygon points="107,125 130,125 130,150" fill="#0a1a33"/>
  <polygon points="1071,125 1096,125 1071,150" fill="#0a1a33"/>
</svg>
<div class="abs step-label" style="left:200px">Step 1</div>
<div class="abs step-label" style="left:533px">Step 2</div>
<div class="abs step-label" style="left:849px">Step 3</div>

<div class="abs content-frame"></div>
<div class="abs step-text" style="left:113px">Enter your zip<br>code.</div>
<div class="abs step-text" style="left:443px">Fill out your vehicle &amp;<br>driver information.</div>
<div class="abs step-text" style="left:765px">Compare<br>rates &amp; <b>SAVE!</b></div>

<div class="abs zip-panel"></div>
<div class="abs zip-label">Enter your Zip coad here</div>
<div class="abs zip-input"></div>
<div class="abs continue">Continue <i></i></div>
<div class="abs badge" role="img" aria-label="Security certificate badge"></div>
<svg class="abs" style="left:378px;top:412px" width="110" height="72" viewBox="0 0 110 72" aria-hidden="true">
  <path d="M10,52 C16,16 56,6 84,32" fill="none" stroke="#d4202a" stroke-width="9" stroke-linecap="round"/>
  <polygon points="68,38 102,60 98,22" fill="#d4202a"/>
</svg>

<div class="abs section-title" style="left:182px;top:560px">Suspendisse quis placerat massa, porta luctus dolor</div>
<div class="abs article">
  <p>Lorem ipsum dolor sit amet, consectetur adipiscing elit. Duis nec ultricies eros. Aliquam nec enim odio. Proin semper sem sollicitudin massa adipiscing, nec egestas tellus egestas. Duis vel erat eget augue iaculis fermentum. Praesent sagittis mauris ut fringilla tempor. Nullam viverra est sem, eu tincidunt quam rutrum eu. Proin ullamcorper arcu consectetur, tincidunt ante id, eleifend nisi. Donec fringilla mi eget purus gravida, id vulputate velit bibendum. In non turpis tincidunt neque imperdiet porta. Donec vel pellentesque eros. Phasellus fringilla scelerisque nisl. Etiam cursus risus ac sem pulvinar rhoncus. Fusce ornare viverra lectus quis fermentum. Fusce porta imperdiet sodales. Lorem ipsum dolor sit amet, consectetur adipiscing elit. Mauris tempus laoreet diam, a aliquet dolor faucibus sit amet.</p>
  <p>Suspendisse quis placerat massa, porta luctus dolor. In in tellus massa. Mauris egestas nunc non blandit fringilla. Duis tincidunt feugiat mauris ut facilisis. Fusce elementum quam at dui luctus, accumsan hendrerit lorem tempor. Pellentesque consequat ultricies lectus, posuere volutpat lacus ultrices sit amet. Cras varius augue sapien, et interdum tellus rutrum vitae. Donec quis lacus dignissim sem scelerisque laoreet. Fusce suscipit ultrices scelerisque. Proin fermentum dui tempus aliquam auctor. Ut nec est et velit euismod rhoncus vel eget erat. Phasellus lobortis justo massa, et interdum elit vehicula imperdiet.</p>
  <p>Fusce ornare viverra lectus quis fermentum. Fusce porta imperdiet sodales. Lorem ipsum dolor sit amet, consectetur adipiscing elit. Mauris tempus laoreet diam, a aliquet dolor faucibus sit amet.</p>
</div>

<div class="abs section-title" style="left:748px;top:560px">Visitor Reviews</div>
<div class="abs review">Nunc non sapien a leo tempus hendrerit. Quisque placerat convallis dui id varius. Mauris justo enim, tristique in pulvinar ut, dignissim at lacus. Proin sagittis odio porta enim malesuada, eget auctor augue lacinia.</div>
<svg class="abs review-tail" width="20" height="16" viewBox="0 0 20 16" aria-hidden="true">
  <polygon points="0,0 18,0 14,14" fill="#ececec"/>
  <polyline points="0,0.5 14,14 18,0.5" fill="none" stroke="#bdbdbd"/>
</svg>
<div class="abs reviewer">Visitor Name Here</div>

<div class="abs fan-box">
  <div class="fan-head">Find us on Friendbook</div>
  <div class="fan-name">Auto Insurance <small>on Friendbook</small></div>
  <div class="fan-like">You like this. <span>Unlike</span></div>
  <div class="fan-rule"></div>
  <div class="fan-count">Corin's Blog has 17 fans</div>
  <div class="fans">
    <div class="fan"><div class="ph" role="img" aria-label="Fan profile photo"></div>Arlo</div>
    <div class="fan"><div class="ph" role="img" aria-label="Fan profile photo"></div>Benno</div>
    <div class="fan"><div class="ph" role="img" aria-label="Fan profile photo"></div>Corin</div>
    <div class="fan"><div class="ph" role="img" aria-label="Fan profile photo"></div>Dario</div>
    <div class="fan"><div class="ph" role="img" aria-label="Fan profile photo"></div>Arlo</div>
    <div class="fan"><div class="ph" role="img" aria-label="Fan profile photo"></div>Corin</div>
    <div class="fan"><div class="ph" role="img" aria-label="Fan profile photo"></div>Emil</div>
    <div class="fan"><div class="ph" role="img" aria-label="Fan profile photo"></div>Felix</div>
    <div class="fan"><div class="ph" role="img" aria-label="Fan profile photo"></div>Gideon</div>
    <div class="fan"><div class="ph" role="img" aria-label="Fan profile photo"></div>Corin</div>
  </div>
  <div class="fan-foot"><i></i>Friendbook social plugin</div>
</div>

<div class="abs footer-nav">Home<span>|</span>Privacy Policy<span>|</span>Terms of Use</div>
<div class="abs copyright">Copyright 2013 Autocoverhub.com All Rights Reserved.</div>
</body>
</html>
```